Visitenkarte und Briefdesign
Zielgruppe
Limousinenservice (Stretchlimousinen)
Aufgabenstellung
Ich benötige eine Visitenkarte und ein Briefdesign in einer edlen Optik.
Auf folgender Seite können Informationen oder Bilder eingeholt werden
www.fahrt-glanzwerk.com
Ich mag einen Hintergrund in einer Lederoptik,( wie das Logo in Anhang, BILD x4)

```html
<!DOCTYPE html>
<html lang="de">
<head>
<meta charset="utf-8">
<title>KR Nobelcars – Briefbogen und Visitenkarte</title>
<link href="https://fonts.googleapis.com/css2?family=Arimo:wght@400;700&display=swap" rel="stylesheet">
<style>
:root{
  --backdrop:#9a9a9a;
  --paper:#ffffff;
  --ink:#1c1c1c;
  --band:#151515;
  --pennant:#232323;
  --card-dark-a:#2e2e2e;
  --card-dark-b:#141414;
  --silver:#bdbdbd;
}
*{margin:0;padding:0;box-sizing:border-box}
html,body{width:1200px;height:821px;overflow:hidden}
body{background:var(--backdrop);font-family:"Arimo",Arial,sans-serif;color:var(--ink);position:relative}

/* Letterhead */
.letterhead{position:absolute;left:182px;top:48px;width:516px;height:732px;background:var(--paper);
  border-left:12px solid var(--band);border-right:7px solid var(--band);box-shadow:0 2px 6px rgba(0,0,0,.35)}
.pennant{position:absolute;display:flex;flex-direction:column;align-items:center;justify-content:center;gap:6px;
  background:var(--pennant);color:var(--silver);font-weight:700;text-align:center}
.letterhead .pennant{left:387px;top:0;width:74px;height:130px;padding-bottom:22px;font-size:9px;
  clip-path:polygon(0 0,100% 0,100% 78%,50% 100%,0 78%)}
.pennant .dot{width:14px;height:14px;border-radius:50%;background:var(--silver)}
.sender-line{position:absolute;left:30px;top:138px;font-size:6.5px;font-weight:700;letter-spacing:.2px}
.recipient{position:absolute;left:30px;top:151px;font-size:10.5px;line-height:14px}
.company-block{position:absolute;right:12px;top:148px;text-align:right}
.company-block .service{font-size:12px;letter-spacing:.3px}
.company-block .name{font-size:13.5px;font-weight:700}
.company-block .person{font-size:10.5px;margin-bottom:14px}
.company-block .contact{font-size:7.5px;line-height:10px}
.company-block .label{font-weight:700;margin-top:7px}
.subject{position:absolute;left:30px;top:252px;font-size:10.5px;font-weight:700;letter-spacing:.2px}
.body-text{position:absolute;left:30px;top:284px;width:330px;font-size:8.6px;line-height:16px}
.body-text p+p{margin-top:4px}
.closing{position:absolute;left:30px;top:540px;font-size:8.6px;line-height:16px}

/* Business card back */
.card{position:absolute;width:400px;height:260px;box-shadow:0 2px 6px rgba(0,0,0,.35)}
.card-back{left:748px;top:285px;background:radial-gradient(circle at 50% 45%,var(--card-dark-a),var(--card-dark-b));
  display:flex;align-items:center;justify-content:center;gap:12px;color:var(--silver);font-size:24px;font-weight:700}
.card-back .dot{width:22px;height:22px;border-radius:50%;background:var(--silver)}

/* Business card front */
.card-front{left:736px;top:540px;background:var(--paper);border-right:9px solid var(--band)}
.card-front .pennant{left:312px;top:0;width:50px;height:80px;padding-bottom:14px;font-size:6px;
  clip-path:polygon(0 0,100% 0,100% 76%,50% 100%,0 76%)}
.card-front .pennant .dot{width:10px;height:10px}
.card-front .head{position:absolute;left:34px;top:28px}
.card-front .service{font-size:13px;letter-spacing:.3px}
.card-front .name{font-size:14.5px;font-weight:700}
.card-front .person{font-size:11.5px}
.card-front .col-left{position:absolute;left:34px;top:106px;font-size:11px;line-height:13px}
.card-front .col-right{position:absolute;right:26px;top:106px;font-size:11px;line-height:13px;text-align:right}
.card-front .label{font-weight:700;margin-top:8px}
.card-front .label:first-child{margin-top:0}
</style>
</head>
<body>

<article class="letterhead">
  <div class="pennant"><span class="dot"></span>KR NOBELCARS</div>
  <div class="sender-line">KR NOBELCARS &nbsp;LINDENER WEG 42 B 48231 VELLHOF</div>
  <address class="recipient" style="font-style:normal">Max Mustermann<br>Mustermannstraße 2<br>24824 Musterhausen</address>
  <div class="company-block">
    <div class="service">LIMOUSINENSERVICE</div>
    <div class="name">KR NOBELCARS</div>
    <div class="person">Jonas Wehrle</div>
    <div class="contact">Lindener Weg 42 B<br>48231 Vellhof</div>
    <div class="contact label">E-Mail</div>
    <div class="contact">info@kr-nobelcars.de</div>
    <div class="contact label">Tel.</div>
    <div class="contact">0170-5550187<br>( 24 Stunden erreichbar)</div>
    <div class="contact label">Internet</div>
    <div class="contact">www.fahrt-glanzwerk.com<br>www.kr-nobelcars.de</div>
  </div>
  <div class="subject">Betreff: Einladung zum X</div>
  <div class="body-text">
    <p>Auch gibt es niemanden, der den Schmerz an sich liebt, sucht oder wünscht, nur, weil er Schmerz ist, es sei denn, es kommt zu zufälligen Umständen, in denen Mühen und Schmerz ihm große Freude bereiten können. Um ein triviales Beispiel zu nehmen, wer von uns unterzieht sich je anstrengender körperlicher Betätigung, außer um Vorteile daraus zu ziehen?</p>
    <p>Aber wer hat irgend ein Recht, einen Menschen zu tadeln, der die Entscheidung trifft, eine Freude zu genießen, die keine unangenehmen Folgen hat, oder einen, der Schmerz vermeidet, welcher keine daraus resultierende Freude nach sich zieht? Auch gibt es niemanden, der den Schmerz an sich liebt, sucht oder wünscht, nur, weil er Schmerz ist, es sei denn, es kommt zu zufälligen Umständen, in denen Mühen und Schmerz ihm große Freude bereiten können.</p>
  </div>
  <div class="closing">mit freundlichen Grüßen<br>Jonas Wehrle</div>
</article>

<section class="card card-back"><span class="dot"></span>KR NOBELCARS</section>

<section class="card card-front">
  <div class="pennant"><span class="dot"></span>KR NOBELCARS</div>
  <div class="head">
    <div class="service">LIMOUSINENSERVICE</div>
    <div class="name">KR NOBELCARS</div>
    <div class="person">Jonas Wehrle</div>
  </div>
  <div class="col-left">
    <div>Lindener Weg 42 B<br>48231 Vellhof</div>
    <div class="label">E-Mail</div>
    <div>info@kr-nobelcars.de</div>
    <div class="label">Tel.</div>
    <div>0170-5550187<br><span style="font-size:9.5px">( 24 Stunden erreichbar)</span></div>
  </div>
  <div class="col-right">
    <div class="label">Internet</div>
    <div>www.fahrt-glanzwerk.com<br>www.kr-nobelcars.de</div>
    <div class="label">Whatsapp</div>
    <div>0170-5550187</div>
  </div>
</section>

</body>
</html>
```